Service business needs Business Card Design

Looking to create a new business card design that is both professional and unique the can highlight the many services we offer throughout the seasons. Our tagline is "The Steadfast Touch"
Licensed & Insured: PA392617 has to be small and on the back side of the card.
On the Front:
FirstName LastName
Title
We offer the following services:
Deck Repair and Maintenance
Deck Cleaning and Staining/Painting
Power Washing/House Washing
Landscape Lighting Installation
Christmas Lighting Installation

```html
<!DOCTYPE html>
<html lang="en">
<head>
<meta charset="utf-8">
<title>Halcyon Services – Business Card Concepts</title>
<link href="https://fonts.googleapis.com/css2?family=Sorts+Mill+Goudy&display=swap" rel="stylesheet">
<style>
  :root{
    --stage:#b9b0a8;
    --teal:#00676a;
    --paper:#ffffff;
    --brand:#1636c8;
    --ink-light:#f2f7f7;
  }
  *{margin:0;padding:0;box-sizing:border-box}
  html,body{width:1200px;height:857px;overflow:hidden;background:var(--stage)}
  body{position:relative;font-family:"Sorts Mill Goudy",Georgia,serif}
  .label-bar{position:absolute;left:0;width:1200px;height:45px;background:var(--teal);color:var(--paper);font-size:28px}
  .label-bar span{position:absolute;top:5px;transform:translateX(-50%);white-space:nowrap}
  .bar-one{top:14px}
  .bar-two{top:431px}
  .card{position:absolute;width:527px;height:339px;background:var(--paper);overflow:hidden}
  .d1-front{left:40px;top:75px}
  .d1-back{left:626px;top:75px}
  .d2-front{left:40px;top:500px}
  .d2-back{left:626px;top:500px}

  .brand-block{position:absolute;left:0;width:100%;text-align:center}
  .brand-name{display:flex;align-items:center;justify-content:center;gap:10px;color:var(--brand);font-size:27px;letter-spacing:1px}
  .brand-mark{width:14px;height:14px;border-radius:50%;background:var(--brand)}
  .tagline{color:var(--teal);font-size:16px;margin-top:10px}

  .service-band{position:absolute;left:0;top:170px;width:527px;height:169px;background:var(--teal);border-radius:0 0 20px 20px;color:var(--ink-light)}
  .service-intro{position:absolute;left:63px;top:2px;font-size:15.5px}
  .service-list{list-style:none}
  .service-list li{position:absolute;display:flex;align-items:center;white-space:nowrap}
  .service-band .service-list li{left:34px;font-size:14.5px}
  .service-band .icon{width:20px;height:22px;margin-right:9px;color:var(--ink-light)}

  .license{position:absolute;color:var(--teal);font-size:11.5px;white-space:nowrap}
  .d1-back .license{left:17px;top:304px}
  .d2-back .license{right:9px;top:302px}

  .side-stripe{position:absolute;left:20px;top:0;width:43px;height:339px;background:var(--teal)}
  .d2-back .service-list li{left:27px;color:var(--teal);font-size:15.5px}
  .d2-back .icon{width:30px;height:32px;color:var(--paper);margin-right:17px}
</style>
</head>
<body>
<svg width="0" height="0" style="position:absolute">
  <defs>
    <symbol id="ic-tools" viewBox="0 0 20 24"><path d="M5 1v5l-2 2v14h2V9l2-3V1H6v4H5z" fill="currentColor"/><rect x="12" y="1" width="3" height="9" fill="currentColor"/><rect x="12.5" y="10" width="2" height="13" fill="currentColor"/></symbol>
    <symbol id="ic-roller" viewBox="0 0 20 24"><rect x="2" y="2" width="16" height="6" rx="1" fill="currentColor"/><path d="M18 5h1v6H10v4" stroke="currentColor" stroke-width="1.5" fill="none"/><rect x="8.5" y="14" width="3" height="9" fill="currentColor"/></symbol>
    <symbol id="ic-washer" viewBox="0 0 20 24"><path d="M11 3C5 3 3 12 3 22" stroke="currentColor" stroke-width="1.2" fill="none"/><rect x="10" y="8" width="8" height="12" rx="2" fill="currentColor"/><circle cx="3" cy="22" r="1.5" fill="currentColor"/></symbol>
    <symbol id="ic-lamp" viewBox="0 0 20 24"><rect x="8" y="1" width="4" height="4" fill="currentColor"/><rect x="9.3" y="5" width="1.4" height="15" fill="currentColor"/><rect x="7.5" y="20" width="5" height="2" fill="currentColor"/></symbol>
    <symbol id="ic-tree" viewBox="0 0 20 24"><path d="M10 2l4 6h-2l4 6h-3l4 6H3l4-6H4l4-6H6z" fill="none" stroke="currentColor" stroke-width="1.1"/><rect x="9" y="20" width="2" height="3" fill="currentColor"/></symbol>
  </defs>
</svg>

<header class="label-bar bar-one"><span style="left:197px">Front</span><span style="left:597px">Design 1</span><span style="left:885px">Back</span></header>

<section class="card d1-front">
  <div class="brand-block" style="top:96px">
    <div class="brand-name"><span class="brand-mark"></span>Halcyon Services</div>
    <div class="tagline">"The Steadfast Touch"</div>
  </div>
  <div class="service-band">
    <p class="service-intro">We offer the following services:</p>
    <ul class="service-list">
      <li style="top:24px"><svg class="icon"><use href="#ic-tools"/></svg>Deck Repair and Maintenance</li>
      <li style="top:52px"><svg class="icon"><use href="#ic-roller"/></svg>Deck Cleaning and Staining/Painting</li>
      <li style="top:81px"><svg class="icon"><use href="#ic-washer"/></svg>Power Washing/House Washing</li>
      <li style="top:109px"><svg class="icon"><use href="#ic-lamp"/></svg>Landscape Lighting Installation</li>
      <li style="top:138px"><svg class="icon"><use href="#ic-tree"/></svg>Christmas Lighting Installation</li>
    </ul>
  </div>
</section>

<section class="card d1-back">
  <p class="license">Licensed &amp; Insured: PA392617</p>
</section>

<header class="label-bar bar-two"><span style="left:205px">Front</span><span style="left:605px">Design 2</span><span style="left:892px">Back</span></header>

<section class="card d2-front">
  <div class="brand-block" style="top:160px">
    <div class="brand-name"><span class="brand-mark"></span>Halcyon Services</div>
    <div class="tagline">"The Steadfast Touch"</div>
  </div>
</section>

<section class="card d2-back">
  <div class="side-stripe"></div>
  <ul class="service-list">
    <li style="top:86px"><svg class="icon"><use href="#ic-tools"/></svg>Deck Repair and Maintenance</li>
    <li style="top:129px"><svg class="icon"><use href="#ic-roller"/></svg>Deck Cleaning and Staining/Painting</li>
    <li style="top:169px"><svg class="icon"><use href="#ic-washer"/></svg>Power Washing/House Washing</li>
    <li style="top:206px"><svg class="icon"><use href="#ic-lamp"/></svg>Landscape Lighting Installation</li>
    <li style="top:244px"><svg class="icon"><use href="#ic-tree"/></svg>Christmas Lighting Installation</li>
  </ul>
  <p class="license">Licensed &amp; Insured: PA392617</p>
</section>
</body>
</html>
```